First of a series of workplace posters- our values statement

To produce a high quality poster of our values, we would like one in a3 and one in a4 both full colour
By utilising the supplied text , the intent is to produce a really striking poster for all our work places, which set out our company values. we are looking for really strong graphical elements which support the message visually . This will be the first of a series of posters, so we are looking to establish at stylistic theme for all with this one. for more on our business,

Target Market(s)

Internal and external audiences, our clients are all tier one companies

Requirements
Must have
• contemporary design rather than conservative, visually striking
• Must be clearly readable from a reasonable distance
Nice to have
• would be nice to tie in to the blue and greens of our logo in similar fashion to our website. www.kbtgreenworks.com
Should not have
• Difficult to read fonts,

```html
<!DOCTYPE html>
<html lang="en">
<head>
<meta charset="utf-8">
<title>KBT Greenworks – Our Values</title>
<link rel="stylesheet" href="https://fonts.googleapis.com/css2?family=Jost:wght@400;700;800&display=swap">
<style>
  :root {
    --green-light: #8dc63f;
    --green-dark: #6aab04;
    --blue-light: #0c4a90;
    --blue-dark: #062d64;
    --navy: #0a3580;
    --white: #ffffff;
    --rule: #3b3c9c;
  }
  * { box-sizing: border-box; margin: 0; padding: 0; }
  html, body { width: 1200px; height: 2336px; overflow: hidden; background: var(--white); }
  body { font-family: "Jost", sans-serif; color: var(--white); }
  .poster { width: 1200px; height: 2336px; display: flex; flex-direction: column; }
  .masthead {
    height: 345px; display: flex; align-items: center; justify-content: center; gap: 22px;
  }
  .brand-dot { width: 96px; height: 96px; border-radius: 50%; background: var(--green-dark); }
  .brand-name { font-size: 86px; font-weight: 700; color: var(--navy); letter-spacing: 1px; }
  .value {
    position: relative; height: 332px; padding: 6px 20px 0 20px;
  }
  .value--green { background: linear-gradient(100deg, var(--green-light), var(--green-dark)); }
  .value--blue { background: linear-gradient(100deg, var(--blue-light), var(--blue-dark)); }
  .value--last { height: 324px; border-bottom: 8px solid var(--rule); }
  .value__title { font-size: 44px; font-weight: 700; line-height: 46px; letter-spacing: 1px; }
  .value__intro { font-size: 27px; line-height: 36px; margin-top: 4px; }
  .value--green .value__intro { color: var(--navy); }
  .value--blue .value__intro { color: var(--green-light); }
  .value__list { list-style: none; font-size: 27px; line-height: 36px; }
  .value__icon { position: absolute; right: 32px; top: 16px; }
  .value__mark { position: absolute; right: 36px; top: 40px; display: flex; align-items: center; gap: 8px; }
  .value__mark-dot { width: 26px; height: 26px; border-radius: 50%; background: var(--white); }
  .value__mark-name { font-size: 30px; font-weight: 700; color: var(--white); }
  .value__stat { position: absolute; right: 26px; top: 24px; font-size: 66px; font-weight: 800; }
</style>
</head>
<body>
<main class="poster">
  <header class="masthead">
    <span class="brand-dot"></span>
    <span class="brand-name">KBT Greenworks</span>
  </header>

  <section class="value value--green">
    <h2 class="value__title">We value our people above<br>everything else.</h2>
    <p class="value__intro">We demonstrate that by :</p>
    <ul class="value__list">
      <li>Providing safe,positive,enjoyable workplaces where everyone feels valued and respected.</li>
      <li>Providing careers, not jobs, we grow together.</li>
      <li>Encouraging inclusion, participation and collaboration</li>
      <li>Recognising and rewarding contribution and excellence</li>
      <li>Supporting our people through tough times</li>
    </ul>
    <svg class="value__icon" width="132" height="112" viewBox="0 0 132 112" aria-hidden="true">
      <g fill="var(--white)">
        <circle cx="30" cy="24" r="18"/><circle cx="102" cy="24" r="18"/>
        <path d="M0 82 a30 30 0 0 1 60 0 v6 H0z"/><path d="M72 82 a30 30 0 0 1 60 0 v6 H72z"/>
        <circle cx="66" cy="40" r="22" stroke="var(--green-dark)" stroke-width="4"/>
        <path d="M26 112 v-12 a40 40 0 0 1 80 0 v12z" stroke="var(--green-dark)" stroke-width="4"/>
      </g>
    </svg>
  </section>

  <section class="value value--blue">
    <h2 class="value__title">All our workplaces are safe work places</h2>
    <p class="value__intro">There is nothing more important to us than our team members going home<br>healthy and safe every day,we won’t accept anything less.We :</p>
    <ul class="value__list">
      <li>Take the time to make our work areas safe, whatever it takes</li>
      <li>Don’t accept shortcuts</li>
      <li>Look out for each other</li>
      <li>Investigate our incidents and learn from them, no repeats.</li>
      <li>Think safe, work safe, go home safe.</li>
    </ul>
    <svg class="value__icon" style="right:56px;top:36px" width="80" height="112" viewBox="0 0 80 112" aria-hidden="true">
      <path fill="var(--white)" fill-rule="evenodd" d="M40 0 a40 40 0 0 1 40 40 c0 26-40 72-40 72 S0 66 0 40 A40 40 0 0 1 40 0z M40 22 a18 18 0 1 0 0.01 0z"/>
    </svg>
  </section>

  <section class="value value--green">
    <h2 class="value__title">The planet benefits from our existence</h2>
    <p class="value__intro">We are relentlessly pursuing our objective of providing our clients with<br>pathways to sustainable development. To achieve our vision we :</p>
    <ul class="value__list">
      <li>Minimise our environmental impact in everything we do</li>
      <li>Actively develop and promote world’s best practices in rehabilitation of disturbed land.</li>
    </ul>
    <svg class="value__icon" style="right:46px;top:22px" width="104" height="104" viewBox="0 0 104 104" aria-hidden="true">
      <g fill="none" stroke="var(--white)" stroke-width="3">
        <circle cx="52" cy="52" r="49"/>
        <ellipse cx="52" cy="52" rx="22" ry="49"/>
        <line x1="3" y1="52" x2="101" y2="52"/>
        <path d="M12 28 h80 M12 76 h80"/>
      </g>
    </svg>
  </section>

  <section class="value value--blue">
    <h2 class="value__title" style="margin-top:14px">We are proud of who we are</h2>
    <p class="value__intro" style="margin-top:12px">Our reputation means the world to us. We:</p>
    <ul class="value__list">
      <li>Treat everyone with respect, and we expect it in return</li>
      <li>Do what we say we will do</li>
      <li>Own our mistakes and we fix them</li>
      <li>Are trustworthy and transparent</li>
    </ul>
    <div class="value__mark"><span class="value__mark-dot"></span><span class="value__mark-name">KBT Greenworks</span></div>
  </section>

  <section class="value value--green">
    <h2 class="value__title" style="margin-top:14px">We set the standard</h2>
    <ul class="value__list" style="margin-top:12px">
      <li>We are uncompromising on quality</li>
      <li>We are the best at what we do, and we do what we are best at</li>
      <li>We are always improving</li>
    </ul>
    <span class="value__stat">100%</span>
  </section>

  <section class="value value--blue value--last">
    <h2 class="value__title" style="margin-top:14px">We succeed together</h2>
    <p class="value__intro" style="line-height:32px;margin-top:10px">We believe in win-win relationships. When our Business is profitable<br>everyone benefits, our shareholders, employees, clients, suppliers and the community<br>At KBT we :</p>
    <ul class="value__list" style="margin-top:8px">
      <li>Work as a team, we get it done together</li>
      <li>are building on our success and growing together</li>
      <li>choose to work with employees, customers, and suppliers who fit our values</li>
    </ul>
    <svg class="value__icon" style="right:58px;top:22px" width="96" height="82" viewBox="0 0 132 112" aria-hidden="true">
      <g fill="var(--white)">
        <circle cx="30" cy="24" r="18"/><circle cx="102" cy="24" r="18"/>
        <path d="M0 82 a30 30 0 0 1 60 0 v6 H0z"/><path d="M72 82 a30 30 0 0 1 60 0 v6 H72z"/>
        <circle cx="66" cy="40" r="22" stroke="var(--blue-dark)" stroke-width="4"/>
        <path d="M26 112 v-12 a40 40 0 0 1 80 0 v12z" stroke="var(--blue-dark)" stroke-width="4"/>
      </g>
    </svg>
  </section>
</main>
</body>
</html>
```